Market online tutoring + Back to School + give Support for students school work K to 12 Grade

To promote my tutoring business online need to create a two sided flyer. Need to get the attention of parents and educators who looking for help to support the digital learning of their students due to COVID-19 lock down. I need to project and differentiate that we offer support for online school with individualized learning . We tutor Elementary to High school students on all subjects you may take a look at my website qnacademyga.com for additional info and also I can provide
Updates

Hi All Due to Covid, we were unable to work on this project on time as originally planned. We were given an extension until March 15 and we will complete it by then. Sorry for any inconvenience and Thank you for your support. -QN Academy

Target Market(s)

Parents and students

Industry/Entity Type

Education

Requirements
Must have
• For online less fine print on the first page. The phone number and support text message. Back to School , Support Online learning KEV/NUR test prep should have some focus
Nice to have
• Discuss the platform We created a platform with live instructor interaction, virtual classroom, instructional videos, assessments, and practice to support every individual student’s need. We are confident in our ability to provide the most effective distance learning experience.
Should not have
• too much clunky and packed with content. Should be easy to read with color

```html
<!DOCTYPE html>
<html lang="en">
<head>
<meta charset="utf-8">
<title>QN Academy – Two-Sided Flyer</title>
<link rel="stylesheet" href="https://fonts.googleapis.com/css2?family=Montserrat:wght@400;500;600;800&family=Poppins:wght@800;900&display=swap">
<style>
  :root{
    --stage:#0b3d52;
    --navy:#1c3a52;
    --red:#d6242f;
    --red-deep:#a51b2a;
    --green:#b3dca0;
    --teal:#3bb4d6;
    --slate:#5a8aa4;
    --ink:#111111;
    --white:#ffffff;
    --photo-a:#8d8782;
    --photo-b:#5f5a57;
  }
  *{box-sizing:border-box;margin:0;padding:0}
  html,body{width:1200px;height:1031px;overflow:hidden;background:var(--stage)}
  body{position:relative;font-family:"Montserrat",sans-serif}

  .flyer{position:absolute;top:168px;width:595px;height:842px;transform:scale(0.8264);transform-origin:0 0;overflow:hidden;background:var(--white)}
  .flyer--front{left:87px}
  .flyer--back{left:622px}
  .flyer svg.shapes{position:absolute;inset:0;width:595px;height:842px}
  .abs{position:absolute}

  .photo{position:absolute;background:linear-gradient(135deg,var(--photo-a),var(--photo-b))}
  .photo--front{inset:0}
  .photo--back{left:295px;top:440px;width:255px;height:360px;background:linear-gradient(160deg,#e9e4dc,#b8aa98 70%,#8a7b6a)}
  .photo-frame{position:absolute;left:281px;top:427px;width:284px;height:380px;background:#1a1a1a}

  .brand{position:absolute;display:flex;align-items:center;gap:14px}
  .brand__dot{width:34px;height:34px;border-radius:50%;background:var(--navy);flex:none}
  .brand__name{font-family:"Montserrat",sans-serif;font-weight:800;font-size:34px;color:var(--navy);letter-spacing:1px;white-space:nowrap}

  .enroll{position:absolute;left:393px;top:70px;width:148px;height:148px;border-radius:50%;background:var(--red);border:6px solid var(--white);box-shadow:0 0 0 3px var(--red);display:flex;flex-direction:column;align-items:center;justify-content:center;color:var(--white);font-family:"Poppins",sans-serif;font-weight:800;line-height:1}
  .enroll__top{font-size:19px}
  .enroll__main{font-size:30px;margin-top:4px}

  .lead{left:182px;top:192px;font-family:"Poppins",sans-serif;font-weight:800;font-size:16.5px;line-height:16px;color:var(--ink);text-transform:uppercase}
  .headline{left:47px;top:446px;font-family:"Poppins",sans-serif;font-weight:900;font-size:43px;line-height:40px;color:var(--white)}
  .intro{left:47px;top:590px;width:240px;font-size:14.5px;line-height:23px;color:var(--white)}
  .intro strong{font-weight:800}
  .support{left:325px;top:652px;font-family:"Poppins",sans-serif;font-weight:800;font-size:20.5px;line-height:24px;color:var(--white)}

  .contact{position:absolute;left:53px;font-size:14.5px;line-height:24px;color:#2a2a2a}
  .contact--front{top:778px}
  .contact--back{top:782px}

  .services-title{left:40px;top:284px;font-family:"Poppins",sans-serif;font-weight:900;font-size:42px;color:var(--ink);letter-spacing:0.5px}
  .services-rule{left:41px;top:348px;width:225px;height:5px;background:var(--ink)}
  .services{position:absolute;left:40px;top:372px;list-style:none}
  .services li{display:flex;align-items:center;gap:9px;height:43px;font-size:18.5px;font-weight:500;color:var(--ink)}
  .services svg{width:13px;height:14px;flex:none}

  .photo-caption{left:322px;top:460px;font-family:"Poppins",sans-serif;font-weight:800;font-size:16.5px;line-height:16px;color:var(--ink);text-transform:uppercase}
</style>
</head>
<body>

<!-- Front side -->
<section class="flyer flyer--front">
  <div class="photo photo--front" role="img" aria-label="Photo: a student at a desk taking a live video lesson with a tutor on a desktop screen"></div>
  <svg class="shapes" viewBox="0 0 595 842" aria-hidden="true">
    <defs>
      <linearGradient id="fBand" x1="0" x2="1" y1="0" y2="0">
        <stop offset="0" stop-color="#b3dca0"/><stop offset="0.6" stop-color="#6fc3c9"/><stop offset="1" stop-color="#3bb4d6"/>
      </linearGradient>
      <linearGradient id="fFoot" x1="0" x2="1">
        <stop offset="0" stop-color="#b3dca0"/><stop offset="0.55" stop-color="#8fbcb0"/><stop offset="1" stop-color="#5a8aa4"/>
      </linearGradient>
      <linearGradient id="fRed" x1="0" x2="1">
        <stop offset="0" stop-color="#e12a2f"/><stop offset="1" stop-color="#a51b2a"/>
      </linearGradient>
    </defs>
    <path fill="url(#fRed)" d="M0,250 C80,300 180,325 280,318 C400,305 450,200 490,120 C520,65 560,40 595,35 V80 C540,100 500,200 450,265 C400,330 300,360 200,362 C110,362 40,350 0,345 Z"/>
    <path fill="url(#fBand)" d="M0,200 C70,260 170,300 270,296 C390,290 430,190 470,110 C500,55 545,15 595,12 V45 C545,55 505,120 470,190 C430,265 370,320 260,318 C150,316 60,285 0,260 Z"/>
    <path fill="#ffffff" d="M0,0 H595 V12 C545,15 500,55 470,110 C430,190 390,290 270,296 C170,300 70,260 0,200 Z"/>
    <path fill="url(#fRed)" d="M0,745 C150,730 300,770 430,780 C510,786 565,740 595,700 V842 H0 Z"/>
    <path fill="url(#fFoot)" d="M0,758 C150,748 300,785 430,795 C515,801 565,770 595,742 V842 H0 Z"/>
  </svg>

  <div class="brand" style="left:62px;top:92px">
    <span class="brand__dot"></span>
    <span class="brand__name">QN ACADEMY</span>
  </div>
  <div class="enroll"><span class="enroll__top">ENROLL</span><span class="enroll__main">NOW</span></div>
  <p class="abs lead">QN Academy<br>provides every<br>student with<br>personal<br>guidance</p>
  <h1 class="abs headline">WE<br>LOVE<br>TEACHING</h1>
  <p class="abs intro"><strong>QN Academy</strong> strives to improve your children's academic achievements and analytical problem solving skills.</p>
  <p class="abs support">WE SUPPORT<br>DIGITAL LEARNING<br>IN THIS COVID-19<br>LOCKDOWN</p>
  <p class="contact contact--front">www.qnacademyga.com<br>Call Us At: 555-014-2287</p>
</section>

<!-- Back side -->
<section class="flyer flyer--back">
  <svg class="shapes" viewBox="0 0 595 842" aria-hidden="true">
    <defs>
      <linearGradient id="bBand" x1="0" x2="1">
        <stop offset="0" stop-color="#b3dca0"/><stop offset="0.6" stop-color="#72c3cc"/><stop offset="1" stop-color="#3bb4d6"/>
      </linearGradient>
      <linearGradient id="bFoot" x1="0" x2="1">
        <stop offset="0" stop-color="#b3dca0"/><stop offset="0.55" stop-color="#8fbcb0"/><stop offset="1" stop-color="#5a8aa4"/>
      </linearGradient>
      <linearGradient id="bRed" x1="0" x2="1">
        <stop offset="0" stop-color="#e12a2f"/><stop offset="1" stop-color="#a51b2a"/>
      </linearGradient>
    </defs>
    <path fill="url(#bRed)" d="M0,228 C200,218 350,232 470,250 C530,258 570,248 595,212 V282 C560,305 500,302 440,292 C300,268 150,246 0,250 Z"/>
    <path fill="url(#bBand)" d="M0,172 C150,192 300,228 420,205 C505,188 510,70 458,0 H595 V212 C570,248 530,258 470,250 C350,232 200,218 0,232 Z"/>
  </svg>

  <div class="brand" style="left:72px;top:82px">
    <span class="brand__dot"></span>
    <span class="brand__name">QN ACADEMY</span>
  </div>

  <h2 class="abs services-title">SERVICES</h2>
  <div class="abs services-rule"></div>
  <ul class="services">
    <li><svg viewBox="0 0 13 14"><path d="M6.5 0 L13 2 V7 C13 10.5 10 13 6.5 14 C3 13 0 10.5 0 7 V2 Z" fill="#111"/></svg>Mathematics (Georgia Standard of Education)</li>
    <li><svg viewBox="0 0 13 14"><path d="M6.5 0 L13 2 V7 C13 10.5 10 13 6.5 14 C3 13 0 10.5 0 7 V2 Z" fill="#111"/></svg>Reading (GSE)</li>
    <li><svg viewBox="0 0 13 14"><path d="M6.5 0 L13 2 V7 C13 10.5 10 13 6.5 14 C3 13 0 10.5 0 7 V2 Z" fill="#111"/></svg>Writing (GSE)</li>
    <li><svg viewBox="0 0 13 14"><path d="M6.5 0 L13 2 V7 C13 10.5 10 13 6.5 14 C3 13 0 10.5 0 7 V2 Z" fill="#111"/></svg>KEV Preparation</li>
    <li><svg viewBox="0 0 13 14"><path d="M6.5 0 L13 2 V7 C13 10.5 10 13 6.5 14 C3 13 0 10.5 0 7 V2 Z" fill="#111"/></svg>Critical Thinking</li>
    <li><svg viewBox="0 0 13 14"><path d="M6.5 0 L13 2 V7 C13 10.5 10 13 6.5 14 C3 13 0 10.5 0 7 V2 Z" fill="#111"/></svg>Computer Science</li>
    <li><svg viewBox="0 0 13 14"><path d="M6.5 0 L13 2 V7 C13 10.5 10 13 6.5 14 C3 13 0 10.5 0 7 V2 Z" fill="#111"/></svg>Robotics</li>
    <li><svg viewBox="0 0 13 14"><path d="M6.5 0 L13 2 V7 C13 10.5 10 13 6.5 14 C3 13 0 10.5 0 7 V2 Z" fill="#111"/></svg>Custom Courses</li>
  </ul>

  <div class="photo-frame"></div>
  <div class="photo photo--back" role="img" aria-label="Photo: a child seated at a home desk following an online class on a computer"></div>
  <p class="abs photo-caption">Don't waste your<br>children precious<br>time in this COVID-19<br>lockdown</p>

  <svg class="shapes" viewBox="0 0 595 842" aria-hidden="true">
    <path fill="url(#bRed)" d="M0,760 C150,740 300,770 430,782 C510,790 565,760 595,722 V842 H0 Z"/>
    <path fill="url(#bFoot)" d="M0,772 C150,752 300,790 430,800 C515,806 565,780 595,752 V842 H0 Z"/>
  </svg>
  <p class="contact contact--back">www.qnacademyga.com<br>Call Us At: 555-014-2287</p>
</section>

</body>
</html>
```